Mini Market Tolvo Business Presentation Cards

We need presentation cards with a logo we already own designed at this website as well. We need the printing, delivery and sleek, modem design in harmony with our previous logo design.

Target Market(s)

Low, med and High income class.

Industry/Entity Type

Grocery Store

Contact Information for Business Card

Business logo (Mini Market Tolvo), name: Esteban L. Morales/Lidia E. Paredes/ Iván Paredes (those are the names for the different cards),
Address: Col. Lomas del Valle, carretera a Tegel a 150mts del Centro Vial. Puerto Cortés, Honduras.
Email: minimarkettolvo@correofalso.hn
Teléfono: (504) 9715-3068

Font styles to use
Serif
Sans Serif

Requirements
Must have
• Business logo (Mini Market Tolvo), person name, department,
• Address, phone number, email address.

```html
<!DOCTYPE html>
<html lang="es">
<head>
<meta charset="UTF-8">
<title>Mini Market Tolvo — Tarjeta de presentación</title>
<link rel="stylesheet" href="https://fonts.googleapis.com/css2?family=Open+Sans:wght@400;700&display=swap">
<style>
  :root {
    --brand-green: #8bbe50;
    --brand-red: #e6432c;
    --ink: #3d3d3d;
    --paper: #ffffff;
  }
  * { margin: 0; padding: 0; box-sizing: border-box; }
  html, body {
    width: 1200px;
    height: 704px;
    overflow: hidden;
    background: var(--paper);
  }
  .card {
    position: relative;
    width: 1200px;
    height: 704px;
    overflow: hidden;
    background: var(--paper);
    font-family: "Open Sans", Arial, sans-serif;
    color: var(--ink);
  }
  .card__backdrop {
    position: absolute;
    inset: 0;
    width: 1200px;
    height: 704px;
  }
  .brand {
    position: absolute;
    top: 50px;
    right: 44px;
    display: flex;
    align-items: center;
    gap: 26px;
  }
  .brand__name {
    color: var(--brand-red);
    font-size: 42px;
    font-weight: 400;
    line-height: 1.2;
    text-align: right;
  }
  .brand__dot {
    width: 188px;
    height: 188px;
    border-radius: 50%;
    background: var(--brand-green);
  }
  .person-name {
    position: absolute;
    left: 64px;
    top: 240px;
    font-size: 50px;
    font-weight: 700;
    color: var(--brand-red);
    letter-spacing: 0.3px;
  }
  .contact {
    position: absolute;
    left: 62px;
    top: 368px;
    list-style: none;
  }
  .contact__item {
    display: flex;
    align-items: flex-start;
    gap: 36px;
    font-size: 28px;
    line-height: 37px;
    margin-bottom: 34px;
  }
  .contact__item--phone { margin-bottom: 28px; }
  .contact__icon {
    flex: 0 0 46px;
    width: 46px;
    height: 46px;
    fill: var(--ink);
  }
</style>
</head>
<body>
  <main class="card">
    <svg class="card__backdrop" viewBox="0 0 1200 704" aria-hidden="true">
      <circle cx="167" cy="535" r="600" fill="var(--brand-green)"/>
    </svg>

    <div class="brand">
      <p class="brand__name">Mini Market<br>Tolvo</p>
      <div class="brand__dot" aria-hidden="true"></div>
    </div>

    <h1 class="person-name">Esteban L. Morales</h1>

    <ul class="contact">
      <li class="contact__item">
        <svg class="contact__icon" viewBox="0 0 24 24" aria-hidden="true">
          <path d="M12 2a7 7 0 0 0-7 7c0 5.2 7 13 7 13s7-7.8 7-13a7 7 0 0 0-7-7zm0 9.6A2.6 2.6 0 1 1 12 6.4a2.6 2.6 0 0 1 0 5.2z"/>
        </svg>
        <span>Col. Lomas del Valle<br>carretera a Tegel a 150mts del Centro Vial.<br>Puerto Cortés, Honduras</span>
      </li>
      <li class="contact__item contact__item--phone">
        <svg class="contact__icon" viewBox="0 0 24 24" aria-hidden="true">
          <path d="M6.6 10.8a15.1 15.1 0 0 0 6.6 6.6l2.2-2.2a1 1 0 0 1 1-.25 11.4 11.4 0 0 0 3.6.57 1 1 0 0 1 1 1V20a1 1 0 0 1-1 1A17 17 0 0 1 3 4a1 1 0 0 1 1-1h3.5a1 1 0 0 1 1 1c0 1.25.2 2.46.57 3.58a1 1 0 0 1-.25 1z"/>
        </svg>
        <span>(504) 9715-3068</span>
      </li>
      <li class="contact__item">
        <svg class="contact__icon" viewBox="0 0 24 24" aria-hidden="true">
          <path d="M2 5h20v1.2l-10 6.3L2 6.2z"/>
          <path d="M2 8.4l10 6.3 10-6.3V19H2z"/>
        </svg>
        <span>minimarkettolvo@correofalso.hn</span>
      </li>
    </ul>
  </main>
</body>
</html>
```